Maple Ridge business card design

Card needs to include the following text/items:
Company Logo
Tobin Marsh
Phone # - 555-318-7642
service@mapleridgelandscaping.example
Lawn & landscape maintenance services

```html
<!DOCTYPE html>
<html lang="en">
<head>
<meta charset="utf-8">
<title>Maple Ridge business card</title>
<link rel="stylesheet" href="https://fonts.googleapis.com/css2?family=Cinzel:wght@400;600;700&family=Open+Sans:wght@400&display=swap">
<style>
  :root {
    --forest: #1e4a2b;
    --olive: #7f9a2e;
    --white: #ffffff;
    --stage: #cfcfcf;
    --sky: #4fb3e6;
    --leaf: #2f7a3a;
  }
  * { margin: 0; padding: 0; box-sizing: border-box; }
  html, body { width: 1200px; height: 800px; overflow: hidden; }
  body {
    background: var(--stage);
    position: relative;
    font-family: "Open Sans", sans-serif;
  }
  .card {
    position: absolute;
    left: 300px;
    width: 600px;
    height: 343px;
    border-radius: 22px;
    overflow: hidden;
    border: 3px solid var(--olive);
  }
  .card--contact { top: 30px; background: var(--white); }
  .card--brand { top: 420px; background: var(--forest); }

  /* contact side */
  .contact-band {
    position: absolute; left: 0; top: 222px;
    width: 420px; height: 86px;
    background: var(--forest);
  }
  .accent-band {
    position: absolute; right: 0; top: 58px;
    width: 170px; height: 50px;
    background: var(--olive);
  }
  .emblem {
    position: absolute;
    border-radius: 50%;
    background: radial-gradient(circle at 40% 30%, var(--sky) 0 30%, var(--leaf) 55%, var(--forest) 100%);
    border: 3px solid var(--olive);
    box-shadow: 0 0 0 6px var(--white);
  }
  .emblem--contact { left: 376px; top: 70px; width: 190px; height: 190px; }
  .person-name {
    position: absolute; left: 40px; top: 150px;
    font-family: "Cinzel", serif; font-weight: 600;
    font-size: 26px; color: var(--olive);
  }
  .contact-list {
    position: absolute; left: 30px; top: 230px;
    list-style: none; color: var(--white); font-size: 15px; line-height: 23px;
  }
  .contact-list li { display: flex; align-items: center; gap: 8px; }
  .contact-list svg { width: 14px; height: 14px; flex: none; }

  /* brand side */
  .emblem--brand { left: 210px; top: 24px; width: 180px; height: 180px; box-shadow: none; }
  .brand-name {
    position: absolute; left: 0; width: 100%; top: 200px;
    text-align: center;
    font-family: "Cinzel", serif; font-weight: 700;
    font-size: 42px; color: var(--white);
  }
  .tagline-band {
    position: absolute; left: 0; top: 268px;
    width: 100%; height: 40px;
    background: var(--olive);
    display: flex; align-items: center; justify-content: center;
    font-family: "Cinzel", serif; font-weight: 600;
    font-size: 18px; letter-spacing: 1px; color: var(--white);
  }
</style>
</head>
<body>
  <section class="card card--contact">
    <div class="accent-band"></div>
    <div class="contact-band"></div>
    <div class="emblem emblem--contact" role="img" aria-label="Round landscape emblem with trees, hills and sun"></div>
    <h1 class="person-name">Tobin Marsh</h1>
    <ul class="contact-list">
      <li>
        <svg viewBox="0 0 24 24"><path fill="#7f9a2e" d="M6.6 10.8a15 15 0 0 0 6.6 6.6l2.2-2.2a1 1 0 0 1 1-.25 11 11 0 0 0 3.6.6 1 1 0 0 1 1 1V20a1 1 0 0 1-1 1A17 17 0 0 1 3 4a1 1 0 0 1 1-1h3.5a1 1 0 0 1 1 1 11 11 0 0 0 .6 3.6 1 1 0 0 1-.25 1z"/></svg>
        555-318-7642
      </li>
      <li>
        <svg viewBox="0 0 24 24"><rect x="2" y="5" width="20" height="14" rx="1" fill="#7f9a2e"/><path d="M2 6l10 7 10-7" stroke="#1e4a2b" stroke-width="2" fill="none"/></svg>
        service@mapleridgelandscaping.example
      </li>
      <li>
        <svg viewBox="0 0 24 24"><circle cx="12" cy="12" r="10" fill="none" stroke="#7f9a2e" stroke-width="2"/><path d="M2 12h20M12 2c4 4 4 16 0 20M12 2c-4 4-4 16 0 20" stroke="#7f9a2e" stroke-width="1.6" fill="none"/></svg>
        www.mapleridgelandscaping.example
      </li>
    </ul>
  </section>

  <section class="card card--brand">
    <div class="emblem emblem--brand" role="img" aria-label="Round landscape emblem with trees, hills and sun"></div>
    <h2 class="brand-name">Maple Ridge</h2>
    <div class="tagline-band">Lawn &amp; Landscape Maintenance Services</div>
  </section>
</body>
</html>
```